Business Cards for an 'affordable luxury' inner city home builder in Calgary.

We need a business card design that emulates the progressive, innovative, culture of our company and the modern style of our homes. Use our website www.velmarcrest-ab.com as a reference for the product we build.

Our company builds homes in the inner city space of Calgary, Alberta. We build affordable luxury.

Target Market(s)

Young professional Families

Contact Information for Business Card

Try to maintain consistency with the logo font and the card font.

Requirements
Must have
• The details must include: Name, education, title, phone number, website and email (Address is not as important)
• The design must be uniques (like our logo), elegant, sophisticated and modern.

```html
<!DOCTYPE html>
<html lang="en">
<head>
<meta charset="utf-8">
<title>Velmarcrest Homes Ltd – Business Card</title>
<link rel="stylesheet" href="https://fonts.googleapis.com/css2?family=Montserrat:wght@500&family=Roboto:wght@400&family=Roboto+Condensed:wght@400;700&display=swap">
<style>
  :root {
    --backdrop: #d6d6d6;
    --paper: #ffffff;
    --ink: #222222;
    --charcoal: #232323;
    --slate: #8a8a8a;
    --mist: #b9b9b9;
    --white: #ffffff;
  }
  * { margin: 0; padding: 0; box-sizing: border-box; }
  html, body {
    width: 1125px; height: 1200px; overflow: hidden;
    background: var(--backdrop);
  }
  .card {
    position: absolute; left: 150px; width: 825px; height: 471px;
  }
  .card--front { top: 98px; background: var(--paper); }
  .card--back { top: 631px; background: var(--charcoal); }

  .brand {
    position: absolute; left: 205px; top: 170px;
    display: flex; align-items: center; gap: 28px;
  }
  .brand__square {
    width: 74px; height: 74px; background: var(--ink);
  }
  .brand__name {
    font-family: "Montserrat", sans-serif; font-weight: 500;
    font-size: 36px; line-height: 37px; letter-spacing: 1px;
    color: var(--ink); text-transform: uppercase;
  }

  .band { position: absolute; left: 0; top: 261px; width: 825px; height: 161px; }

  .contact {
    position: absolute; left: 38px; top: 295px;
    font-family: "Roboto", sans-serif; font-size: 19px; color: #2b2b2b;
    list-style: none;
  }
  .contact__address { margin-bottom: 10px; }
  .contact__item { display: flex; align-items: center; gap: 9px; height: 25px; }
  .contact__icon { width: 16px; height: 16px; flex: none; }

  .person {
    position: absolute; right: 43px; top: 267px; text-align: right;
    font-family: "Roboto Condensed", sans-serif; color: var(--white);
  }
  .person__name { font-weight: 700; font-size: 30px; line-height: 36px; margin-bottom: 2px; }
  .person__line { font-size: 18.5px; line-height: 25px; }

  .back-brand {
    position: absolute; left: 0; right: 0; top: 150px; text-align: center;
    font-family: "Montserrat", sans-serif; font-weight: 500; color: var(--white);
    text-transform: uppercase; letter-spacing: 3px;
  }
  .back-brand__name { font-size: 46px; line-height: 56px; }
  .back-brand__sub { font-size: 46px; line-height: 56px; }
  .back-url {
    position: absolute; left: 0; right: 0; top: 393px; text-align: center;
    font-family: "Roboto", sans-serif; font-size: 20px; letter-spacing: 9px;
    color: var(--white);
  }
</style>
</head>
<body>
  <section class="card card--front">
    <div class="brand">
      <div class="brand__square"></div>
      <div class="brand__name">Velmarcrest<br>Homes Ltd</div>
    </div>

    <svg class="band" viewBox="0 0 825 161" aria-hidden="true">
      <polygon points="0,0 428,0 379,161 0,161" fill="var(--slate)"/>
      <polygon points="433,0 825,0 825,161 384,161" fill="var(--charcoal)"/>
    </svg>

    <ul class="contact">
      <li class="contact__address">418 14 Ave NE, Calgary, AB</li>
      <li class="contact__item">
        <svg class="contact__icon" viewBox="0 0 16 16" aria-hidden="true"><path d="M3.5 1.5l2.5 0 1 3.5-1.8 1.2c.8 1.8 2.2 3.2 4 4l1.2-1.8 3.5 1v2.5c0 .8-.7 1.5-1.5 1.5C6.6 13.4 2.6 9.4 2 3c0-.8.7-1.5 1.5-1.5z" fill="#2b2b2b"/></svg>
        403-555-0148
      </li>
      <li class="contact__item">
        <svg class="contact__icon" viewBox="0 0 16 16" aria-hidden="true"><rect x="1.5" y="4" width="13" height="9" fill="#2b2b2b"/><path d="M1.5 4l6.5 5 6.5-5" fill="none" stroke="#8a8a8a" stroke-width="1.2"/></svg>
        projects@velmarcrest-ab.com
      </li>
      <li class="contact__item">
        <svg class="contact__icon" viewBox="0 0 16 16" aria-hidden="true"><circle cx="8" cy="8" r="6.5" fill="#2b2b2b"/><path d="M4 6c2 0 2 2 4 2s1 3 3 3M9 3c0 2 3 2 3 4" fill="none" stroke="#8a8a8a" stroke-width="1.2"/></svg>
        www.velmarcrest-ab.com
      </li>
    </ul>

    <div class="person">
      <div class="person__name">Ravinder</div>
      <div class="person__line">Co-Founder</div>
      <div class="person__line">Business Development / Strategy</div>
      <div class="person__line">Professional Engineer (P.ENG)</div>
      <div class="person__line">Masters of Business Administration (MBA)</div>
    </div>
  </section>

  <section class="card card--back">
    <div class="back-brand">
      <div class="back-brand__name">Velmarcrest</div>
      <div class="back-brand__sub">Homes Ltd</div>
    </div>
    <div class="back-url">www.velmarcrest-ab.com</div>
  </section>
</body>
</html>
```